UPDATE 2: I HAVE ATTACHED TWO PHOTOS; PLEASE CONSIDER USING EITHER ONE IN A NEW DESIGN. THANK YOU.
UPDATE: I HAVE INCLUDED 4 SAMPLE BOOK COVERS THAT I LIKE TO HELP YOU ORIENT YOUR DESIGN WORK
Looking for book cover, spine, and back for a MEMOIR. Details:
TITLE: Mama's Quiet Orchard
AUTHOR: Lorivel Brashton
GENRE: Memoir
STYLE REQUESTED: Abstract and colorful; designers are welcome to get creative. Note that the memoir takes place largely in a poor African American city.
BOOK SUMMARY: As a young girl, Lorivel Brashton—or “Rivvy” to her friends and family—discovers the man she thought was her father wasn’t, and her real biological father wants little if anything to do with her. What follows is the story of a girl’s longing, a longing disturbed by abuse, disappointment, and loneliness.
Set against the backdrop of Gary, Indiana—the then “murder capital of the world”—Mama’s Quiet Orchard follows Lorivel as she searches and grows, following a path that eventually leads her to self-discovery and self-confidence.
Template provided for InDesign. Please note margins and bleed areas. Make sure any letters/words are at least one inch from edges. On spine, leave three inches at bottom for publisher's logo.
Updates
To all designers: Please note that there should NOT be any images of people as part of your designs. Thank you, and my apologies for not mentioning that in the initial ask.

```html
<!DOCTYPE html>
<html lang="en">
<head>
<meta charset="utf-8">
<title>Mama's Quiet Orchard — Lorivel Brashton</title>
<link href="https://fonts.googleapis.com/css2?family=Josefin+Sans:wght@400;600&display=swap" rel="stylesheet">
<style>
  :root {
    --sky-blue: #3fa6d8;
    --sky-mist: #bfe0ea;
    --sky-pale: #f6efcf;
    --sky-gold: #f2bf4c;
    --ridge-peach: #ee9d72;
    --ridge-rose: #d98385;
    --ridge-mauve: #a9708e;
    --ridge-plum: #8c5a7c;
    --town-gold: #c89a34;
    --town-ochre: #a77a22;
    --band-brown: #3b2710;
    --ink-brown: #3a2810;
    --name-gold: #b8892e;
  }
  * { margin: 0; padding: 0; box-sizing: border-box; }
  html, body { width: 800px; height: 1200px; overflow: hidden; background: var(--band-brown); }
  .cover {
    position: relative;
    width: 800px;
    height: 1200px;
    overflow: hidden;
    background: var(--band-brown);
    font-family: "Josefin Sans", sans-serif;
  }
  .sunset-sky {
    position: absolute;
    left: 0; top: 0;
    width: 800px; height: 470px;
    background:
      radial-gradient(ellipse 300px 28px at 180px 70px, rgba(255,255,255,0.55), transparent 70%),
      radial-gradient(ellipse 260px 20px at 560px 110px, rgba(255,255,255,0.45), transparent 70%),
      radial-gradient(ellipse 340px 26px at 300px 190px, rgba(255,248,225,0.6), transparent 70%),
      linear-gradient(180deg,
        var(--sky-blue) 0%,
        var(--sky-mist) 16%,
        var(--sky-pale) 42%,
        #f6da88 64%,
        var(--sky-gold) 100%);
  }
  .mountain-ridges {
    position: absolute;
    left: 0; top: 440px;
    width: 800px; height: 360px;
    background:
      radial-gradient(ellipse 520px 60px at 560px 40px, rgba(236,150,110,0.8), transparent 75%),
      linear-gradient(180deg,
        rgba(242,191,76,0) 0%,
        var(--ridge-peach) 14%,
        #e69178 30%,
        var(--ridge-rose) 46%,
        #c07a8e 62%,
        var(--ridge-mauve) 78%,
        var(--ridge-plum) 100%);
  }
  .city-skyline {
    position: absolute;
    left: 0; top: 760px;
    width: 800px; height: 220px;
    background:
      linear-gradient(180deg,
        var(--ridge-plum) 0%,
        #b78a55 12%,
        var(--town-gold) 24%,
        var(--town-ochre) 52%,
        #6e4c1a 76%,
        var(--band-brown) 100%);
  }
  .title {
    position: absolute;
    left: 0; top: 122px;
    width: 800px;
    text-align: center;
    color: var(--ink-brown);
    font-weight: 600;
    font-size: 80px;
    line-height: 100px;
    letter-spacing: 0.2em;
    text-transform: uppercase;
  }
  .title-line { display: block; padding-left: 0.2em; }
  .author {
    position: absolute;
    left: 0; top: 1000px;
    width: 800px;
    text-align: center;
    color: var(--name-gold);
    font-weight: 400;
    font-size: 50px;
    line-height: 64px;
    letter-spacing: 0.28em;
    text-transform: uppercase;
  }
  .author-line { display: block; padding-left: 0.28em; }
</style>
</head>
<body>
  <main class="cover">
    <div class="sunset-sky" role="img" aria-label="Blue sky with wispy clouds fading into a golden sunset"></div>
    <div class="mountain-ridges" role="img" aria-label="Layered hazy mountain ridges in peach, rose and mauve"></div>
    <div class="city-skyline" role="img" aria-label="Silhouette of a crowded city of flat-roofed buildings and power lines in gold and dark brown"></div>
    <h1 class="title">
      <span class="title-line">Mama's</span>
      <span class="title-line">Quiet</span>
      <span class="title-line">Orchard</span>
    </h1>
    <p class="author">
      <span class="author-line">Lorivel</span>
      <span class="author-line">Brashton</span>
    </p>
  </main>
</body>
</html>
```